Business Card Design Project

I need a new business card design for my building/development company: Kestrel Ridge Builders.

We specialise in small sub-divisions, multi-story developments and new house builds.
We handle the whole process from concept stage right throught to a fully developed property.
Updates

Target Market(s)

people looking to develop their property and need help. New property buyers

Industry/Entity Type

House

Requirements
Must have
• My logo on both sides:
Side 1: Logo taking up whole side as per old card but with a color/style change.

Side 2: Contact page: include logo but the rest just surprise me!

All contact details will be: (and need to be changable for each employee) I'll inform you of specifics before printing.

Name Surname
Position ie. Managing director
M: insert mobile
E: insert email
P.O. Box 518, Ashwell, Vic, 3094
www.kestrelridgebuilders.com.au

Nice to have
• Colors i'd like: (not necessarily all but this is the basic idea)

Black, blue, grey, silver, white

```html
<!DOCTYPE html>
<html lang="en">
<head>
<meta charset="utf-8">
<title>Kestrel Ridge Builders – Business Card</title>
<link href="https://fonts.googleapis.com/css2?family=Arimo:ital,wght@0,400;0,700;1,400;1,700&display=swap" rel="stylesheet">
<style>
  :root {
    --brand-blue: #0a7bcc;
    --ink: #111111;
    --paper: #ffffff;
  }
  html, body {
    margin: 0;
    padding: 0;
    overflow: hidden;
    background: var(--paper);
  }
  .card {
    position: relative;
    width: 1200px;
    height: 777px;
    background: var(--paper);
    overflow: hidden;
    font-family: "Arimo", Arial, sans-serif;
    color: var(--ink);
  }
  .person-name {
    position: absolute;
    left: 72px;
    top: 110px;
    margin: 0;
    font-size: 60px;
    font-weight: 700;
    letter-spacing: 1.5px;
    color: var(--brand-blue);
    line-height: 1;
  }
  .person-role {
    position: absolute;
    left: 73px;
    top: 212px;
    margin: 0;
    font-size: 36px;
    font-weight: 700;
    font-style: italic;
    letter-spacing: 1.2px;
    line-height: 1;
  }
  .contact-list {
    position: absolute;
    left: 73px;
    top: 306px;
    margin: 0;
    padding: 0;
    list-style: none;
    font-size: 30px;
    line-height: 39.5px;
  }
  .contact-label {
    color: var(--brand-blue);
    font-style: italic;
  }
  .web-address {
    position: absolute;
    left: 474px;
    top: 714px;
    margin: 0;
    font-size: 36px;
    letter-spacing: 3.4px;
    color: var(--brand-blue);
    white-space: nowrap;
    line-height: 1;
    transform-origin: left bottom;
    transform: rotate(-52deg);
  }
  .brand-mark {
    position: absolute;
    left: 830px;
    top: 470px;
    width: 150px;
    height: 150px;
  }
  .brand-block {
    position: absolute;
    right: 70px;
    top: 638px;
    text-align: right;
  }
  .brand-name {
    margin: 0;
    font-size: 40px;
    font-weight: 700;
    color: var(--brand-blue);
    line-height: 1;
    white-space: nowrap;
  }
  .brand-tagline {
    margin: 8px 0 0;
    font-size: 21px;
    letter-spacing: 0.3px;
    color: var(--ink);
    line-height: 1;
    white-space: nowrap;
  }
</style>
</head>
<body>
  <main class="card">
    <h1 class="person-name">Marcus Hallett</h1>
    <p class="person-role">Managing Director</p>
    <ul class="contact-list">
      <li><span class="contact-label">Mob:</span> 0412 555 019</li>
      <li><span class="contact-label">Email:</span> kestrelridge@mailhub.net.au</li>
      <li><span class="contact-label">P.O.</span> Box 518, Ashwell, Vic, 3094</li>
    </ul>
    <p class="web-address">www.kestrelridgebuilders.com.au</p>
    <svg class="brand-mark" viewBox="0 0 150 150" role="img" aria-label="Company logo mark">
      <rect x="0" y="0" width="150" height="150" fill="var(--brand-blue)"/>
    </svg>
    <div class="brand-block">
      <p class="brand-name">Kestrel Ridge Builders</p>
      <p class="brand-tagline">renovation-construction-development</p>
    </div>
  </main>
</body>
</html>
```